Crowdsourced Research Platform: KOVAL Polls

KOVAL Polls is an acronym for Kindred Opinion Views Among Lands (KOVAL) Polls. This is a research effort to format and combine multiple sources of public opinion data from around the world into merged datasets. The website will at first mainly act as a quality control hub and distribution point for official dataset releases. It will provide resources such as codebooks, development guidelines, and instructional videos for crowdsourcing continued expansion of the resource. We need a coded (HTML and CSS) website design and associated files to launch the website with ease. We purchased the domain www.kovalpolls.org, but access is blocked while it is under construction.

The website design should be based on a logo recently commissioned (see attached). The design should be simple and professional with lots of white space. We would like the logo on the top left of all pages and the primary navigation menu along the top-right of all pages. The primary navigation menu should have a simple mouse-over effect and the main menu items should expand with secondary drop-down options. The footer should include a few columns with headings and links to different pages. The website layout should be dynamic and expand its width to fit different sized screens. There will be a lot of data and information displayed in tables, so we would like the CSS coding and website design to include tables designed to match the website theme. The main graphical content will be data visualisations such as pie/bar charts, histograms, scatter plots, heat maps, moving average trend lines etc. We would therefore like the design to include modular sections (boxes matching theme to display plots/graphs/etc) that can visually display these types of figures with text/caption underneath to explain the data visualizations.

For more information and written placeholder content, designers should read the attached documents to get a better idea about the project. Some draft working papers using merged datsets have been included for reference and you can use these for their examples of data visualizations and use the written content for filling in page content.

Target Market(s)

The primary target audience will be academics in universities and research institutes. The resource will be most useful to quantitative social scientists, particularly political scientists and sociologists, but any discipline concerned with us humans could find the resource useful. Others such as graduate-level university students, civil servants in government departments, members of research institutions, and policy researchers in non-profit organizations will also find the resource useful.

Coding

Coded - Design and coding required

Number of Pages Required

3 page

Font styles to use
Sans Serif

Colors

Designer to choose colors to be used in the design.

Requirements
Must have
• HTML and CSS coding (not Wordpress)
Nice to have
• Content boxes to display data visualizations alongside articles.

```html
<!DOCTYPE html>
<html lang="en">
<head>
<meta charset="utf-8">
<title>KOVAL Polls</title>
<link href="https://fonts.googleapis.com/css2?family=Lato:wght@400;700;900&family=Montserrat:wght@400;500;600&display=swap" rel="stylesheet">
<style>
:root{
  --brand:#1763c0;
  --brand-dark:#0f4fa3;
  --title:#1a5fb4;
  --band:#1565c0;
  --section-blue:#1f86d6;
  --menu:#1652ab;
  --grey-band:#f1f1f1;
  --text:#4a4a4a;
  --table-head:#555555;
  --row-alt:#f3f3f3;
  --footer:#1b3b9e;
  --footer-2:#1f4fb5;
  --footer-bottom:#15318c;
  --white:#ffffff;
}
*{margin:0;padding:0;box-sizing:border-box}
html,body{width:1200px;height:3629px;overflow:hidden}
body{position:relative;background:var(--white);font-family:"Lato",sans-serif;color:var(--text)}
.abs{position:absolute}

/* header */
.site-header{left:0;top:0;width:1200px;height:80px;background:var(--white);border-bottom:4px solid var(--brand)}
.brand{left:78px;top:24px;display:flex;align-items:center;gap:10px;font-family:"Lato",sans-serif;font-weight:700;font-size:24px;color:var(--brand)}
.brand-dot{width:22px;height:22px;border-radius:50%;background:var(--brand)}
.main-nav{top:35px;font-family:"Montserrat",sans-serif;font-size:12.5px;font-weight:500;color:#2d4f8a;letter-spacing:.3px}
.main-nav.active{color:var(--brand)}
.main-nav::after{content:"";display:inline-block;width:5px;height:5px;border-right:1.5px solid currentColor;border-bottom:1.5px solid currentColor;transform:rotate(45deg);margin-left:7px;position:relative;top:-3px}
.dropdown{left:685px;top:73px;width:273px;height:133px;background:var(--menu);padding-top:20px}
.dropdown li{list-style:none;height:28px;padding-left:16px;font-family:"Montserrat",sans-serif;font-size:12px;font-weight:500;color:var(--white);letter-spacing:.3px;display:flex;align-items:center}
.dropdown li::before{content:"";width:5px;height:5px;border-right:1.5px solid #fff;border-top:1.5px solid #fff;transform:rotate(45deg);margin-right:22px}

/* hero */
.hero-map{left:0;top:85px;width:1200px;height:423px;background:linear-gradient(180deg,#ffffff 0%,#eef3fa 100%)}
.hero-map .land{position:absolute;left:250px;top:20px;width:880px;height:380px;border-radius:40% 45% 35% 40%;background:radial-gradient(ellipse at 50% 45%,#4a78c2 0%,#2a5aa8 55%,#c9d8ee 100%);opacity:.9}
.hero-map .legend{position:absolute;left:85px;top:18px;width:34px;height:385px;background:linear-gradient(180deg,#12316f,#9fb9e2,#ffffff);border:1px solid #333}

.cta-band{left:0;top:513px;width:1200px;height:97px;background:var(--band);display:flex;align-items:center}
.cta-band p{position:absolute;left:210px;font-size:29px;color:var(--white);letter-spacing:.3px}
.btn-light{position:absolute;left:837px;top:32px;width:153px;height:39px;background:var(--white);color:#1b2d55;font-weight:700;font-size:13px;display:flex;align-items:center;justify-content:center;letter-spacing:.4px}

/* feature sections */
.slant-band{left:0;top:1011px;width:1200px;height:510px}
.feature-title{font-family:"Lato",sans-serif;font-weight:700;font-size:28px;color:var(--title);letter-spacing:.5px;text-transform:uppercase}
.feature-copy{font-size:13.5px;line-height:24px;color:var(--text);width:520px}
.btn-blue{width:180px;height:39px;background:linear-gradient(90deg,#2a8ad8,#1458b4);color:var(--white);font-weight:700;font-size:13px;display:flex;align-items:center;justify-content:center;letter-spacing:.4px}
.photo{border-radius:2px}
.frame-corner{width:40px;height:40px;border-color:var(--brand);border-style:solid}
.slider-arrow{width:14px;height:14px;border-right:3px solid #fff;border-top:3px solid #fff}

/* datasets */
.datasets{left:0;top:1941px;width:1200px;height:615px;background:var(--section-blue)}
.datasets h2{position:absolute;left:0;top:55px;width:1200px;text-align:center;font-family:"Montserrat",sans-serif;font-weight:500;font-size:26px;color:var(--white)}
.data-card{top:116px;width:329px;height:424px;background:var(--white);box-shadow:0 2px 6px rgba(0,0,0,.15)}
.chart-box{position:absolute;left:22px;top:17px;width:285px;height:194px;border:1px solid #c8c8c8;background:#fff}
.card-title{position:absolute;left:0;top:226px;width:100%;text-align:center;font-weight:700;font-size:18px;color:var(--title);letter-spacing:.4px}
.card-text{position:absolute;left:20px;top:254px;width:289px;text-align:center;font-size:13.5px;line-height:22px;color:var(--text)}
.card-btn{position:absolute;left:90px;top:353px;width:150px;height:39px;background:linear-gradient(90deg,#2a8ad8,#1458b4);color:#fff;font-weight:700;font-size:13px;display:flex;align-items:center;justify-content:center}

/* table */
.table-title{left:0;top:2625px;width:1200px;text-align:center;font-weight:700;font-size:29px;color:var(--title);letter-spacing:.5px}
.table-lead{left:0;top:2682px;width:1200px;text-align:center;font-size:13.5px;color:#333}
.data-table{left:75px;top:2727px;width:1053px;border-collapse:collapse;font-size:13.5px;color:#444}
.data-table th{background:var(--table-head);color:var(--white);font-family:"Montserrat",sans-serif;font-weight:500;font-size:13.5px;height:53px;text-align:left;padding-left:14px;border-right:1px solid #777}
.data-table td{height:47px;padding-left:14px;border-right:1px solid #d6d6d6}
.data-table tr:nth-child(even) td{background:var(--row-alt)}
.data-table tbody{border:1px solid #d6d6d6}

/* footer */
.site-footer{left:0;top:3214px;width:1200px;height:339px;background:linear-gradient(90deg,var(--footer),var(--footer-2))}
.footer-bottom{left:0;top:3553px;width:1200px;height:76px;background:var(--footer-bottom);display:flex;align-items:center;justify-content:center;font-size:12.5px;color:#b9c6ea}
.footer-heading{font-family:"Montserrat",sans-serif;font-size:18px;color:var(--white);letter-spacing:.4px}
.footer-links{list-style:none;font-family:"Montserrat",sans-serif;font-size:14px;color:#e2e8f8}
.footer-links li{height:34px}
.contact-label{font-family:"Montserrat",sans-serif;font-size:14px;color:#dfe6f7;line-height:19px}
.social{width:22px;height:22px;border-radius:50%;background:var(--white)}
</style>
</head>
<body>

<header class="abs site-header">
  <div class="abs brand"><span class="brand-dot"></span>KOVAL Polls</div>
  <span class="abs main-nav active" style="left:721px">HOME</span>
  <span class="abs main-nav" style="left:812px">RESOURCES</span>
  <span class="abs main-nav" style="left:936px">SUPPORT</span>
  <span class="abs main-nav" style="left:1046px">RESEARCH</span>
</header>

<section class="abs hero-map" role="img" aria-label="World choropleth map shaded in blues by survey coverage, with a vertical colour legend from 0 to 239">
  <div class="legend"></div>
  <div class="land"></div>
  <span style="position:absolute;left:124px;top:10px;font-size:13px;color:#222">239</span>
  <span style="position:absolute;left:124px;top:394px;font-size:13px;color:#222">0</span>
</section>

<ul class="abs dropdown">
  <li>ABOUT</li><li>VISION</li><li>PARTICIPATE</li><li>CONTACT</li>
</ul>

<section class="abs cta-band">
  <p>Aliquam ac magna nec lorem euismod congue</p>
  <span class="btn-light">LEARN MORE</span>
</section>

<!-- about -->
<h2 class="abs feature-title" style="left:75px;top:679px">About KOVAL Survey</h2>
<p class="abs feature-copy" style="left:75px;top:733px">KOVAL Polls make it easier to work with multiple sources of public opinion data. It does so by formatting variables for consistency and merging datasets together. The current merged dataset includes millions of respondents, covers most countries in the world, and extends back decades. This increased variation over time and space enables answering new research questions with greater reliability.</p>
<span class="abs btn-blue" style="left:75px;top:925px">READ MORE</span>

<div class="abs frame-corner" style="left:614px;top:688px;border-width:6px 0 0 6px"></div>
<div class="abs frame-corner" style="left:1084px;top:688px;border-width:6px 6px 0 0"></div>
<div class="abs frame-corner" style="left:614px;top:922px;border-width:0 0 6px 6px"></div>
<div class="abs frame-corner" style="left:1084px;top:922px;border-width:0 6px 6px 0"></div>
<div class="abs photo" style="left:627px;top:700px;width:488px;height:255px;background:linear-gradient(135deg,#6d8fb8,#c9d3df 55%,#8a9bb0)" role="img" aria-label="Photo of hands reviewing charts on a tablet beside printed reports"></div>
<div class="abs slider-arrow" style="left:640px;top:819px;transform:rotate(-135deg)"></div>
<div class="abs slider-arrow" style="left:1088px;top:819px;transform:rotate(45deg)"></div>

<!-- slanted band -->
<svg class="abs slant-band" viewBox="0 0 1200 510" width="1200" height="510" aria-hidden="true">
  <polygon points="0,0 1200,54 1200,509 0,453" fill="#f1f1f1"/>
</svg>
<h2 class="abs feature-title" style="left:75px;top:1110px">Etiam Dictum Urna Sagittis</h2>
<p class="abs feature-copy" style="left:75px;top:1166px">Variables are available at three levels of analysis within each corresponding dataset: respondent, country-survey, and county-year. At the respondent level, common variables are binary and result from dichotomizing different answer scales. Neutral and midpoint answers are consistently grouped with negative answers, meaning that respondent level variables focus on measuring the presence of what it measures rather than its absence.</p>
<span class="abs btn-blue" style="left:75px;top:1357px">READ MORE</span>
<div class="abs photo" style="left:629px;top:1111px;width:496px;height:336px;background:linear-gradient(160deg,#3b4f6a,#9fb2c8 45%,#e4e8ee)" role="img" aria-label="Photo of a team in a meeting room on a video conference with charts on screens"></div>

<!-- third feature -->
<div class="abs photo" style="left:77px;top:1566px;width:511px;height:305px;background:linear-gradient(120deg,#5d5a55,#8d8a84 50%,#a39a8c)" role="img" aria-label="Photo of a person in a blanket sitting on a street holding a cardboard sign"></div>
<h2 class="abs feature-title" style="left:617px;top:1574px">Etiam Dictum Urna Sagittis</h2>
<p class="abs feature-copy" style="left:617px;top:1626px">Variables are available at three levels of analysis within each corresponding dataset: respondent, country-survey, and county-year. At the respondent level, common variables are binary and result from dichotomizing different answer scales. Neutral and midpoint answers are consistently grouped with negative answers, meaning that respondent level variables focus on measuring the presence of what it measures rather than its absence.</p>
<span class="abs btn-blue" style="left:617px;top:1822px">READ MORE</span>

<!-- datasets -->
<section class="abs datasets">
  <h2>KOVAL Polls Datasets</h2>

  <article class="abs data-card" style="left:75px">
    <div class="chart-box">
      <svg width="285" height="194" viewBox="0 0 285 194">
        <rect x="30" y="12" width="240" height="160" fill="none" stroke="#bbb"/>
        <g fill="#2f6fb8" opacity=".8">
          <circle cx="50" cy="160" r="3"/><circle cx="62" cy="152" r="3"/><circle cx="70" cy="158" r="3"/><circle cx="78" cy="146" r="3"/><circle cx="85" cy="140" r="3"/><circle cx="90" cy="150" r="3"/><circle cx="96" cy="132" r="3"/><circle cx="102" cy="138" r="3"/><circle cx="108" cy="124" r="3"/><circle cx="112" cy="130" r="3"/><circle cx="118" cy="112" r="3"/><circle cx="124" cy="120" r="3"/><circle cx="128" cy="104" r="3"/><circle cx="134" cy="110" r="3"/><circle cx="140" cy="96" r="3"/><circle cx="146" cy="90" r="3"/><circle cx="150" cy="100" r="3"/><circle cx="156" cy="82" r="3"/><circle cx="162" cy="76" r="3"/><circle cx="168" cy="86" r="3"/><circle cx="174" cy="66" r="3"/><circle cx="180" cy="72" r="3"/><circle cx="186" cy="58" r="3"/><circle cx="192" cy="50" r="3"/><circle cx="198" cy="62" r="3"/><circle cx="204" cy="44" r="3"/><circle cx="110" cy="142" r="3"/><circle cx="130" cy="126" r="3"/><circle cx="152" cy="112" r="3"/><circle cx="170" cy="98" r="3"/><circle cx="188" cy="80" r="3"/><circle cx="255" cy="28" r="3"/>
        </g>
      </svg>
    </div>
    <h3 class="card-title">MAECENAS VEHICULA</h3>
    <p class="card-text">Etiam dictum, urna sagittis iaculis blandit, tellus ligula lacinia purus, eget pharetra ligula ex et dolor.</p>
    <span class="card-btn">LEARN MORE</span>
  </article>

  <article class="abs data-card" style="left:436px">
    <div class="chart-box">
      <svg width="285" height="194" viewBox="0 0 285 194">
        <g fill="#2a63b8">
          <rect x="26" y="130" width="38" height="52"/><rect x="76" y="112" width="38" height="70"/><rect x="126" y="96" width="38" height="86"/><rect x="176" y="104" width="38" height="78"/><rect x="226" y="80" width="38" height="102"/>
        </g>
        <polyline points="45,92 95,78 145,62 195,66 245,38" fill="none" stroke="#3f86d6" stroke-width="2"/>
        <g fill="#3f86d6"><circle cx="45" cy="92" r="4"/><circle cx="95" cy="78" r="4"/><circle cx="145" cy="62" r="4"/><circle cx="195" cy="66" r="4"/><circle cx="245" cy="38" r="4"/></g>
        <g fill="#fff" font-family="Lato,sans-serif" font-size="9" text-anchor="middle">
          <text x="45" y="177">2014</text><text x="95" y="177">2015</text><text x="145" y="177">2016</text><text x="195" y="177">2017</text><text x="245" y="177">2018</text>
        </g>
      </svg>
    </div>
    <h3 class="card-title">MAECENAS VEHICULA</h3>
    <p class="card-text">Etiam dictum, urna sagittis iaculis blandit, tellus ligula lacinia purus, eget pharetra ligula ex et dolor.</p>
    <span class="card-btn">LEARN MORE</span>
  </article>

  <article class="abs data-card" style="left:794px">
    <div class="chart-box">
      <svg width="285" height="194" viewBox="0 0 285 194">
        <line x1="26" y1="14" x2="26" y2="176" stroke="#999"/><line x1="26" y1="176" x2="272" y2="176" stroke="#999"/>
        <g fill="#1f6fc0">
          <rect x="36" y="100" width="9" height="76"/><rect x="54" y="60" width="9" height="116"/><rect x="72" y="130" width="9" height="46"/><rect x="90" y="112" width="9" height="64"/><rect x="108" y="70" width="9" height="106"/><rect x="126" y="140" width="9" height="36"/><rect x="144" y="96" width="9" height="80"/><rect x="162" y="124" width="9" height="52"/><rect x="180" y="40" width="9" height="136"/><rect x="198" y="84" width="9" height="92"/><rect x="216" y="50" width="9" height="126"/><rect x="234" y="118" width="9" height="58"/><rect x="252" y="74" width="9" height="102"/>
        </g>
      </svg>
    </div>
    <h3 class="card-title">MAECENAS VEHICULA</h3>
    <p class="card-text">Etiam dictum, urna sagittis iaculis blandit, tellus ligula lacinia purus, eget pharetra ligula ex et dolor.</p>
    <span class="card-btn">LEARN MORE</span>
  </article>
</section>

<!-- table -->
<h2 class="abs table-title">QUISQUE RISUS MAGNA</h2>
<p class="abs table-lead">Lorem ipsum dolor sit amet, consectetur adipiscing elit. Duis ut tortor vitae lorem venenatis rutrum.</p>
<table class="abs data-table">
  <colgroup><col style="width:44px"><col style="width:232px"><col style="width:259px"><col style="width:254px"><col style="width:264px"></colgroup>
  <thead><tr><th>No</th><th>Customer Name</th><th>Items</th><th>Subject Code</th><th>Subject Code</th></tr></thead>
  <tbody>
    <tr><td>1</td><td>Daniel Morrow</td><td>Mauris laoreet commodo</td><td>Mauris laoreet commodo</td><td>Mauris laoreet commodo</td></tr>
    <tr><td>2</td><td>Daniel Morrow</td><td>Mauris laoreet commodo</td><td>Mauris laoreet commodo</td><td>Mauris laoreet commodo</td></tr>
    <tr><td>3</td><td>Daniel Morrow</td><td>Mauris laoreet commodo</td><td>Mauris laoreet commodo</td><td>Mauris laoreet commodo</td></tr>
    <tr><td>4</td><td>Daniel Morrow</td><td>Mauris laoreet commodo</td><td>Mauris laoreet commodo</td><td>Mauris laoreet commodo</td></tr>
    <tr><td>5</td><td>Daniel Morrow</td><td>Mauris laoreet commodo</td><td>Mauris laoreet commodo</td><td>Mauris laoreet commodo</td></tr>
    <tr><td>6</td><td>Daniel Morrow</td><td>Mauris laoreet commodo</td><td>Mauris laoreet commodo</td><td>Mauris laoreet commodo</td></tr>
    <tr><td>7</td><td>Daniel Morrow</td><td>Mauris laoreet commodo</td><td>Mauris laoreet commodo</td><td>Mauris laoreet commodo</td></tr>
  </tbody>
</table>

<!-- footer -->
<footer class="abs site-footer">
  <h4 class="abs footer-heading" style="left:75px;top:50px">CONTACT US</h4>
  <svg class="abs" style="left:75px;top:106px" width="24" height="18" viewBox="0 0 24 18" aria-hidden="true"><rect x="1" y="1" width="22" height="16" fill="none" stroke="#fff" stroke-width="2"/><polyline points="1,1 12,10 23,1" fill="none" stroke="#fff" stroke-width="2"/></svg>
  <p class="abs contact-label" style="left:106px;top:98px">EMAIL ADDRESS<br>info@kovalpolls.org</p>
  <svg class="abs" style="left:75px;top:171px" width="20" height="20" viewBox="0 0 24 24" aria-hidden="true"><path fill="#fff" d="M6.6 10.8a15.1 15.1 0 0 0 6.6 6.6l2.2-2.2c.3-.3.7-.4 1-.2 1.1.4 2.3.6 3.6.6.6 0 1 .4 1 1V20c0 .6-.4 1-1 1C10.6 21 3 13.4 3 4c0-.6.4-1 1-1h3.5c.6 0 1 .4 1 1 0 1.3.2 2.5.6 3.6.1.3 0 .7-.2 1z"/></svg>
  <p class="abs contact-label" style="left:106px;top:166px">PHONE NUMBER<br>555.014.2280</p>
  <h4 class="abs footer-heading" style="left:75px;top:240px">STAY IN TOUCH</h4>
  <span class="abs social" style="left:78px;top:288px"></span>
  <span class="abs social" style="left:123px;top:288px"></span>
  <span class="abs social" style="left:168px;top:288px"></span>
  <span class="abs social" style="left:213px;top:288px"></span>

  <h4 class="abs footer-heading" style="left:411px;top:50px">ABOUT</h4>
  <ul class="abs footer-links" style="left:411px;top:98px"><li>Home</li><li>About Us</li><li>Services</li><li>Career</li></ul>
  <h4 class="abs footer-heading" style="left:646px;top:50px">RESOURCES</h4>
  <ul class="abs footer-links" style="left:646px;top:98px"><li>Support</li><li>Why Us</li><li>Help</li><li>FAQ</li></ul>
  <h4 class="abs footer-heading" style="left:883px;top:50px">SUBLINKS</h4>
  <ul class="abs footer-links" style="left:883px;top:98px"><li>Fermentum</li><li>Et lorem</li><li>Nunc porta</li><li>Convallis pede</li></ul>
</footer>
<div class="abs footer-bottom">Copyright © 2018 KOVAL Polls. All right reserved</div>

</body>
</html>
```